Flyer for Aluminium recycling business

We are a startup aluminium recycling business. We don’t have a logo yet. I’ve attached a flyer created by one of our sales people but it’s a bit average and we need something a bit more modern and slick. You have creative license to completely change everything - as long as the information being communicated is the same.

Target Market(s)

Hospitality, Hotels, Apartment blocks, malls etcs

Industry/Entity Type

Aluminium recycling

Requirements
Must have
• the wording
Nice to have
• you have free license on design aspect

```html
<!DOCTYPE html>
<html lang="en">
<head>
<meta charset="utf-8">
<title>Greenloop Metals – Aluminium Recycling Flyer</title>
<link href="https://fonts.googleapis.com/css2?family=Montserrat:wght@700;800;900&family=Poppins:wght@400;500;600;700&family=Allura&display=swap" rel="stylesheet">
<style>
  :root{
    --leaf:#3bb54a;
    --leaf-light:#43bd4f;
    --forest:#0b4a17;
    --forest-deep:#063b10;
    --forest-mid:#0e5a1c;
    --ink:#0a2e10;
    --lime:#d6de23;
    --lime-dark:#c8d11c;
    --alert:#e5173f;
    --head-top:#e3f0c4;
    --head-bottom:#f1f8e2;
    --paper:#fbfdf6;
    --white:#ffffff;
  }
  *{margin:0;padding:0;box-sizing:border-box}
  html,body{width:827px;height:1200px;overflow:hidden;background:var(--paper)}
  .flyer{position:relative;width:827px;height:1200px;overflow:hidden;font-family:"Poppins",sans-serif;color:var(--ink);background:var(--paper)}

  /* header */
  .hero{position:absolute;left:0;top:0;width:827px;height:452px;background:linear-gradient(160deg,var(--head-top) 0%,var(--head-bottom) 70%,#f6fbee 100%)}
  .brand{position:absolute;left:62px;top:60px;display:flex;align-items:center;gap:10px}
  .brand-dot{width:34px;height:34px;border-radius:50%;background:var(--leaf)}
  .brand-name{font-family:"Montserrat",sans-serif;font-weight:800;font-size:21px;letter-spacing:.5px;color:var(--forest)}
  .headline{position:absolute;left:66px;top:148px;font-family:"Montserrat",sans-serif;line-height:1}
  .headline .lead{display:block;font-weight:800;font-size:29px;color:var(--ink);letter-spacing:-.3px}
  .headline .big{display:block;font-weight:900;font-size:53px;letter-spacing:-1.5px;margin-top:6px}
  .headline .green{color:var(--leaf)}
  .headline .dark{color:var(--ink)}
  .script{position:absolute;left:244px;top:316px;font-family:"Allura",cursive;font-size:66px;color:var(--leaf);transform:rotate(-4deg);line-height:1}
  .tagline{position:absolute;left:69px;top:398px;padding-left:8px;border-left:2px solid var(--forest);font-size:15px;line-height:19px;color:var(--ink)}
  .hero-art{position:absolute;left:462px;top:8px;width:336px;height:430px;border-radius:24px;background:radial-gradient(ellipse at 60% 55%,#f39a3c 0%,#e9872b 22%,#7cc25a 45%,#e3f0c4 75%)}

  /* process */
  .pay-note{position:absolute;left:69px;top:484px;width:175px;font-size:12.6px;font-weight:600;line-height:15.2px;color:var(--ink)}
  .pay-art{position:absolute;left:140px;top:594px;width:66px;height:78px;border-radius:12px;background:linear-gradient(135deg,#7fd36a,#2f9e3d 60%,#e39a3a)}
  .route{position:absolute;left:0;top:452px;width:827px;height:514px}
  .step{position:absolute;font-size:12.6px;font-weight:600;line-height:15px;color:var(--ink)}
  .step-1{left:396px;top:486px}
  .step-2{left:396px;top:515px;width:345px}
  .step-4{left:250px;top:880px;width:204px;text-align:right}
  .step-3{left:538px;top:879px;width:150px}
  .badge{position:absolute;width:22px;height:22px;border-radius:50%;font-size:11px;font-weight:700;display:flex;align-items:center;justify-content:center}
  .badge-lime{background:var(--lime);color:var(--ink)}
  .badge-dark{background:var(--forest);color:var(--white)}
  .badge-leaf{background:var(--leaf);color:var(--white)}
  .here{position:absolute;left:292px;top:590px;width:84px;font-family:"Poppins",sans-serif;font-weight:700;font-size:16px;line-height:16px;color:var(--white);text-align:center}

  /* examples */
  .examples{position:absolute;left:0;top:966px;width:827px;height:234px;background:linear-gradient(90deg,var(--forest-mid) 0 418px,var(--forest-deep) 418px 100%)}
  .examples-title{position:absolute;left:209px;top:945px;width:407px;height:38px;border-radius:19px;background:var(--leaf);border:2px solid var(--white);color:var(--white);font-weight:700;font-size:19.5px;display:flex;align-items:center;justify-content:center;letter-spacing:.2px}
  .take-list{position:absolute;list-style:none;color:var(--white);font-size:13px;line-height:16px}
  .take-list li{position:relative;padding-left:19px;margin-bottom:6.5px}
  .take-list li::before{content:"";position:absolute;left:0;top:2px;width:13px;height:13px;border-radius:50%;background:var(--leaf)}
  .take-list li::after{content:"";position:absolute;left:4px;top:5px;width:3px;height:6px;border:solid var(--white);border-width:0 1.6px 1.6px 0;transform:rotate(45deg)}
  .take-left{left:110px;top:1007px;left:110px}
  .take-left{left:110px}
  .take-list.take-left{left:179px;left:179px}
  .contact{position:absolute;left:171px;top:1105px;width:484px;height:38px;border:1.5px solid var(--white);border-radius:19px;display:flex;align-items:center;justify-content:center;gap:12px;color:var(--white);font-weight:700;font-size:16.5px}
  .contact .divider{width:1.5px;height:20px;background:var(--leaf)}
  .contact svg{display:block}
  .contact span{display:flex;align-items:center;gap:7px}
</style>
</head>
<body>
<main class="flyer">

  <section class="hero">
    <div class="brand">
      <div class="brand-dot"></div>
      <div class="brand-name">GREENLOOP METALS</div>
    </div>
    <h1 class="headline">
      <span class="lead">PLAYING THE FAIR</span>
      <span class="big green">ALUMINIUM</span>
      <span class="big dark">RECYCLING</span>
      <span class="big dark">GAME</span>
    </h1>
    <div class="script">for good</div>
    <p class="tagline">Our patrenship alth you is based on common<br>sense,mutual gain and a better tomorrow</p>
    <div class="hero-art" role="img" aria-label="Worker in green overalls dropping a bag into an orange recycling bin with a rake beside it, banknotes floating around"></div>
  </section>

  <p class="pay-note">We pay you for however much of that resource your waste has generated and give you a report on that, so you can see how good you are</p>

  <svg class="route" viewBox="0 452 827 514" aria-hidden="true">
    <!-- guide lines -->
    <path d="M376 536 V570 H612 A138 138 0 0 1 750 708" fill="none" stroke="#c8d11c" stroke-width="1.5"/>
    <path d="M750 708 A138 138 0 0 1 612 846 H514 V886" fill="none" stroke="#3bb54a" stroke-width="1.5"/>
    <path d="M480 886 V846 H200 A72 72 0 0 1 128 774 V726" fill="none" stroke="#0b4a17" stroke-width="1.5"/>

    <!-- red arrow -->
    <path d="M108 592 C96 625 112 652 142 660" fill="none" stroke="#e5173f" stroke-width="4" stroke-linecap="round"/>
    <path d="M134 650 L148 662 L131 668 Z" fill="#e5173f"/>

    <!-- top lane -->
    <rect x="246" y="582" width="132" height="78" fill="#e5173f"/>
    <path d="M376 582 H612 A126 126 0 0 1 738 708 H660 A48 48 0 0 0 612 660 H376 Z" fill="#d6de23"/>
    <rect x="496" y="582" width="120" height="78" fill="#cfd81f"/>
    <path d="M376 614 L382 621 L376 628 Z" fill="#e5173f"/>

    <!-- pin -->
    <path d="M266 580 C245 580 236 598 240 612 C244 628 258 640 268 662 C278 640 292 628 296 612 C300 598 288 580 266 580 Z" fill="#c4102f"/>
    <circle cx="268" cy="605" r="11" fill="#ffffff"/>

    <!-- bottom lanes -->
    <path d="M738 708 A126 126 0 0 1 612 834 H496 V758 H612 A48 48 0 0 0 660 708 Z" fill="#3bb54a"/>
    <rect x="496" y="758" width="120" height="76" fill="#33ab44"/>
    <path d="M496 758 H226 A15 15 0 0 1 211 743 V622 L173 602 L135 622 V774 A60 60 0 0 0 195 834 H496 Z" fill="#0b4a17"/>
    <rect x="376" y="758" width="120" height="76" fill="#0e561b"/>
    <path d="M738 708 L726 708 L732 716 Z" fill="#d6de23"/>

    <!-- bags -->
    <g fill="#111">
      <circle cx="424" cy="630" r="16"/><circle cx="448" cy="628" r="18"/>
      <path d="M418 612 L430 612 L424 620 Z"/><path d="M442 606 L456 606 L449 614 Z"/>
    </g>
    <!-- cans -->
    <g fill="#111">
      <rect x="528" y="604" width="16" height="34" rx="3"/>
      <rect x="548" y="614" width="12" height="24" rx="2"/><rect x="551" y="607" width="6" height="8"/>
      <rect x="564" y="624" width="26" height="14" rx="2"/><rect x="562" y="620" width="30" height="5" rx="1"/>
    </g>
    <!-- bin -->
    <g fill="#111">
      <rect x="672" y="640" width="26" height="34" rx="2"/>
      <rect x="668" y="634" width="34" height="6" rx="1"/>
      <rect x="681" y="629" width="8" height="5"/>
    </g>
    <!-- truck -->
    <g fill="#0b3d12">
      <rect x="600" y="726" width="34" height="22" rx="2"/>
      <path d="M636 732 H648 L656 742 V748 H636 Z"/>
      <circle cx="610" cy="750" r="5"/><circle cx="646" cy="750" r="5"/>
    </g>
    <!-- factory -->
    <path d="M528 816 V794 L542 786 V794 L556 786 V794 L570 786 V770 H578 V816 Z" fill="#0b4a17"/>
    <!-- ingots -->
    <g fill="none" stroke="#d6de23" stroke-width="2.5">
      <path d="M420 802 h14 v12 h-14 z M438 802 h14 v12 h-14 z M428 788 h14 v12 h-14 z"/>
      <path d="M434 802 l8-6 M452 802 l6-5 M442 788 l6-5"/>
    </g>
    <!-- no mining -->
    <circle cx="315" cy="796" r="28" fill="none" stroke="#e5173f" stroke-width="5"/>
    <rect x="298" y="796" width="30" height="10" rx="4" fill="#d6de23"/>
    <path d="M312 796 L322 780 L334 786" fill="none" stroke="#d6de23" stroke-width="4"/>
    <line x1="297" y1="776" x2="333" y2="816" stroke="#e5173f" stroke-width="5"/>
    <!-- plant -->
    <path d="M157 764 A16 16 0 0 0 189 764 Z" fill="#d6de23"/>
    <path d="M173 764 V748" stroke="#d6de23" stroke-width="3"/>
    <path d="M173 752 C160 752 158 742 160 738 C168 738 173 744 173 752 Z M173 750 C186 748 188 740 186 734 C178 736 173 742 173 750 Z" fill="#d6de23"/>
  </svg>

  <div class="pay-art" role="img" aria-label="Stack of banknotes and coins with a blue security shield"></div>
  <div class="here">YOU<br>ARE<br>HERE</div>

  <div class="badge badge-lime" style="left:355px;top:483px">1</div>
  <p class="step step-1">We bring you a free bin</p>
  <div class="badge badge-lime" style="left:355px;top:514px">2</div>
  <p class="step step-2">You throw all and any aluminium waste into the bin-no need to super-clean it. Try to compact/squash the aluminium as much as possible</p>

  <p class="step step-4">We turn the aluminium waste into a desirable resource</p>
  <div class="badge badge-dark" style="left:469px;top:886px">4</div>
  <div class="badge badge-leaf" style="left:503px;top:886px">3</div>
  <p class="step step-3">We collect the bin at no charge</p>

  <section class="examples">
    <ul class="take-list" style="left:110px;top:49px;position:absolute">
      <li>Used beverage cans-any</li>
      <li>Tinfoil-scrunched, crusty, burned or dirty</li>
      <li>Disposable BBQ roasting trays</li>
    </ul>
    <ul class="take-list" style="left:180px;top:49px;position:absolute;left:443px">
      <li>Aluminium takeaway containers</li>
      <li>Wine bottle screw tops (and collars-If you<br>can get them off)</li>
      <li>Tear-off can lids</li>
    </ul>
  </section>
  <div class="examples-title">EXAMPLES OF WHAT WE CAN TAKE</div>

  <div class="contact">
    <span>
      <svg width="14" height="14" viewBox="0 0 24 24"><path d="M6.6 10.8a15 15 0 0 0 6.6 6.6l2.2-2.2a1 1 0 0 1 1-.25 11 11 0 0 0 3.6.6 1 1 0 0 1 1 1V20a1 1 0 0 1-1 1A17 17 0 0 1 3 4a1 1 0 0 1 1-1h3.5a1 1 0 0 1 1 1 11 11 0 0 0 .6 3.6 1 1 0 0 1-.25 1z" fill="#3bb54a"/></svg>
      020 555 0148
    </span>
    <i class="divider"></i>
    <span>
      <svg width="18" height="13" viewBox="0 0 18 13"><rect x="0.75" y="0.75" width="16.5" height="11.5" rx="1" fill="none" stroke="#3bb54a" stroke-width="1.5"/><path d="M1 1 L9 7.5 L17 1" fill="none" stroke="#3bb54a" stroke-width="1.5"/></svg>
      hello@greenloopmetals.co.nz
    </span>
  </div>

</main>
</body>
</html>
```